Aviation Maintenance Business Card Design Challenge

We are seeking a compelling and professional business card design for the owner of a newly established company, Harborline Aero, LLC, based out of KTVM – Dunmore Valley Airport (Holloway Field) in Lawrenceville, Georgia. The company specializes in aircraft maintenance and detailing services, providing top-tier care and precision to both private and corporate aircraft owners. This business card will represent the owner, founder and operator, a licensed A&P (Airframe and Powerplant) Mechanic with over 20 years of hands-on aviation maintenance experience. His reputation is built on technical expertise, reliability, and a commitment to excellence — qualities that Harborline Aero aims to reflect in every aspect of its brand, including its visual identity.

Designers are encouraged to include elements such as the KTVM airport code, contact info layout suitable for mobile and field-based communication, and company branding that balances technical skill with personalized service.

Target Market(s)

Aircraft owners and operators

Industry/Entity Type

Aviation

Contact Information for Business Card

Name: Ty Marcus Ferrell, (555) 314-2706, harborlineaerollc@mailnest.example, www.harborlineaero.example, KTVM – Dunmore Valley Airport (Holloway Field) Lawrenceville, Georgia 30099

Requirements
Must have
• Aeronautical themes or visual cues, highlight the company’s dual services: maintenance and cleaning/detailing, emphasize the owner's credentials, experience, and role as the face of the business
Nice to have
• Company logo

```html
<!DOCTYPE html>
<html lang="en">
<head>
<meta charset="utf-8">
<title>Harborline Aero – Business Card</title>
<link href="https://fonts.googleapis.com/css2?family=Montserrat:wght@400;500;700&display=swap" rel="stylesheet">
<style>
  :root {
    --navy: #2e2a8c;
    --sky: #6fdcf7;
    --ink: #1b1b2a;
    --paper: #ffffff;
    --backdrop: #3c3c3e;
  }
  * { box-sizing: border-box; margin: 0; padding: 0; }
  html, body { width: 1200px; height: 875px; overflow: hidden; }
  body {
    background: var(--backdrop);
    font-family: "Montserrat", sans-serif;
    display: flex;
    align-items: center;
    justify-content: center;
    gap: 50px;
  }
  .card {
    position: relative;
    width: 525px;
    height: 300px;
    background: var(--paper);
    border-radius: 24px;
    overflow: hidden;
    box-shadow: 0 14px 30px rgba(0,0,0,.35);
  }
  .card__band { position: absolute; inset: 0; width: 100%; height: 100%; }

  .brand {
    position: absolute;
    display: flex;
    flex-direction: column;
    color: var(--navy);
    white-space: nowrap;
  }
  .brand__name { display: flex; align-items: center; gap: 12px; font-weight: 700; }
  .brand__dot { border-radius: 50%; background: var(--sky); flex: none; }
  .brand__tagline { font-weight: 400; color: var(--navy); }

  .card--front .brand { left: 0; right: 0; top: 96px; align-items: center; }
  .card--front .brand__name { font-size: 34px; }
  .card--front .brand__dot { width: 30px; height: 30px; }
  .card--front .brand__tagline { font-size: 15px; margin-top: 8px; margin-left: 42px; }

  .card--back .brand { right: 34px; top: 26px; align-items: flex-end; }
  .card--back .brand__name { font-size: 22px; gap: 10px; }
  .card--back .brand__dot { width: 20px; height: 20px; }
  .card--back .brand__tagline { font-size: 11px; margin-top: 4px; }

  .person { position: absolute; left: 36px; top: 112px; }
  .person__name { color: var(--navy); font-weight: 700; font-size: 26px; }
  .person__role { color: var(--ink); font-size: 14px; margin-top: 4px; }
  .divider { position: absolute; left: 36px; right: 30px; top: 182px; border-top: 1.5px solid var(--ink); }

  .contact { position: absolute; left: 36px; top: 196px; list-style: none; font-size: 12px; color: var(--ink); }
  .contact li { display: flex; align-items: center; gap: 9px; margin-bottom: 9px; }
  .contact svg { width: 14px; height: 14px; flex: none; }

  .address { position: absolute; right: 30px; top: 194px; text-align: right; font-size: 12px; color: var(--ink); line-height: 1.5; }
  .website { position: absolute; right: 26px; bottom: 9px; color: var(--paper); font-size: 13px; font-weight: 500; }
</style>
</head>
<body>
  <section class="card card--front" aria-label="Card front">
    <svg class="card__band" viewBox="0 0 525 300" preserveAspectRatio="none" aria-hidden="true">
      <polygon points="0,286 300,286 310,278 525,278 525,300 0,300" fill="var(--sky)"/>
      <polygon points="300,300 320,280 525,280 525,300" fill="var(--navy)"/>
    </svg>
    <div class="brand">
      <div class="brand__name"><span class="brand__dot"></span>Harborline Aero</div>
      <p class="brand__tagline">Aircraft Maintenance &amp; Detailing</p>
    </div>
  </section>

  <section class="card card--back" aria-label="Card back">
    <svg class="card__band" viewBox="0 0 525 300" preserveAspectRatio="none" aria-hidden="true">
      <polygon points="0,290 300,290 306,284 525,284 525,300 0,300" fill="var(--sky)"/>
      <polygon points="0,294 290,294 312,264 525,264 525,300 0,300" fill="var(--navy)"/>
    </svg>
    <div class="brand">
      <div class="brand__name"><span class="brand__dot"></span>Harborline Aero</div>
      <p class="brand__tagline">Aircraft Maintenance &amp; Detailing</p>
    </div>

    <div class="person">
      <h1 class="person__name">Ty Marcus Ferrell</h1>
      <p class="person__role">Owner · A&amp;P Mechanic · 20+ Years</p>
    </div>
    <div class="divider"></div>

    <ul class="contact">
      <li>
        <svg viewBox="0 0 24 24" aria-hidden="true"><circle cx="12" cy="12" r="11" fill="var(--navy)"/><path d="M8 6.5l2 .3.9 2.6-1.3 1a7 7 0 003 3l1-1.3 2.6.9.3 2c-.4.9-1.3 1.3-2.3 1.2A9 9 0 016.8 8.8C6.7 7.8 7.1 6.9 8 6.5z" fill="#fff"/></svg>
        (555) 314-2706
      </li>
      <li>
        <svg viewBox="0 0 24 24" aria-hidden="true"><rect x="2" y="5" width="20" height="14" rx="1.5" fill="var(--navy)"/><path d="M3 6l9 7 9-7" stroke="#fff" stroke-width="2" fill="none"/></svg>
        harborlineaerollc@mailnest.example
      </li>
    </ul>

    <p class="address">KTVM – Dunmore Valley Airport<br>(Holloway Field)<br>Lawrenceville, Georgia 30099</p>
    <p class="website">www.harborlineaero.example</p>
  </section>
</body>
</html>
```